LunaGowns.com Banner AD

We are looking for some talented creators to create for us a banner ad for our online clothing store that specializes in dresses. We are looking for a fresh, clean, and sleek KORA, P&Q, and Glint appeal- clean, modern and sophisticated.

We would like for the final project to appear professionally done, we've had projects completed by several talent out there that did not capture our image, and let's just say it was too cluttered and appeared as if a high school editor had completed it.

I have attached a few files for you to reference, I have File 1, 2, 3, 8 and the P&Q photos as examples of what we DO like.

I have attached File 5, which is the work of one the designers that was working on this project. Although it is very simple and gets the point across, it doesn't come across like a magazine editorial.

I have attached File 6, that is the main photo we wish to use for our banner.

I have attached File 7, which is what a creator had done for us via Brevora.com, that is a good example of what we do NOT want.

That is about sums it up! I hope the examples are useful tools for you!

Hi Designers!

Thank you so much for your submissions! I enjoy viewing each and every one of them! Please view my update on what I am looking for, I have made some adjustments and have added a few more examples to reference, I have made my direction a bit more clearer. Because it seems some designers are not quite understanding my direction. I know you all have amazing talent and I am hoping to see something I am looking for and I love soon! If you have any other questions, please don't hesitate to ask! 

Target Market(s)

Our company targets women of all ages, we carry dresses that cater to every occasion, whether its an older woman looking for a dress to attend a wedding or a teenager looking for a prom dress. We want our front page banner to appear fresh, clean, with a feminine touch, we want to stray from tacky (gradients, etc..) and keep it classy all while maintaining that magazine editorial element, we want to be more fashion focused, like Glint. We want this project to appear professionally done. Our desired concept is something out of a magazine editorial, not too much going on, while shifting focus more on the dress itself than a design element like flowers or spring backgrounds.

Industry/Entity Type

High School

Requirements
Must have
• We want a glint fashion appeal, magazine editorial type of look. The phrases below should be included"

"New Season New Sexy Dresses"

"Free U.S shipping on orders $75+"
"Shop our sales up to 60% off"

All of the other phrases do not need to be included. Also, Do not include the parenthesis.
Should not have
• Only include the photo I've attached that appears solo. Please do not include the other 3 dresses that is displayed in a banner that was created for us by another designer. (that is provided as an example only)

```html
<!DOCTYPE html>
<html lang="en">
<head>
<meta charset="utf-8">
<title>Spring Dress Banner</title>
<link rel="stylesheet" href="https://fonts.googleapis.com/css2?family=Jost:wght@400;500&family=Pinyon+Script&display=swap">
<style>
  :root {
    --page: #ffffff;
    --ink: #3a3838;
    --pink: #e3217a;
    --pink-deep: #d11a6b;
    --pink-band: #f07db3;
    --pink-soft: #f9d3e4;
    --pink-mist: #fdeef5;
    --grey-mist: #e7e7e8;
    --white: #ffffff;
  }
  * { margin: 0; padding: 0; box-sizing: border-box; }
  html, body {
    width: 1200px;
    height: 1061px;
    overflow: hidden;
    background: var(--page);
  }
  .stage {
    position: relative;
    width: 1200px;
    height: 1061px;
  }
  .banner {
    position: absolute;
    left: 0;
    top: 9px;
    width: 700px;
    height: 608px;
    transform: scale(1.7143);
    transform-origin: 0 0;
    overflow: hidden;
    background: linear-gradient(160deg, var(--grey-mist) 0%, var(--white) 38%, var(--pink-mist) 70%, var(--pink-soft) 100%);
    font-family: "Jost", "Futura", sans-serif;
    color: var(--ink);
  }
  .backdrop { position: absolute; inset: 0; }
  .headline {
    position: absolute;
    left: 40px;
    top: 28px;
    width: 460px;
    font-family: "Pinyon Script", cursive;
    font-size: 58px;
    line-height: 1.3;
    color: var(--pink);
    white-space: nowrap;
    -webkit-text-stroke: 0.6px var(--pink);
  }
  .title {
    position: absolute;
    left: 40px;
    width: 424px;
    text-align: center;
    font-weight: 400;
    font-size: 50px;
    line-height: 1;
    letter-spacing: -0.5px;
  }
  .title--one { top: 142px; }
  .title--two { top: 203px; }
  .tagline {
    position: absolute;
    left: 74px;
    width: 368px;
    top: 277px;
    text-align: center;
    font-size: 28px;
    line-height: 1.1;
  }
  .underline { position: absolute; left: 70px; top: 310px; }
  .offers { position: absolute; left: 0; top: 370px; }
  .offer {
    position: absolute;
    top: 385px;
    text-align: center;
    color: var(--white);
  }
  .offer--sale { left: 30px; width: 180px; }
  .offer--ship { left: 240px; width: 216px; top: 390px; }
  .offer__label { font-size: 24px; line-height: 1.25; }
  .offer__figure { font-size: 42px; line-height: 1.25; text-shadow: 0 1px 2px rgba(120, 20, 60, 0.35); }
  .step {
    position: absolute;
    top: 350px;
    width: 38px;
    height: 38px;
    border-radius: 50%;
    background: var(--pink);
    border: 2px solid var(--white);
    color: var(--white);
    font-weight: 500;
    font-size: 24px;
    line-height: 33px;
    text-align: center;
  }
  .step--one { left: 89px; }
  .step--two { left: 316px; }
  .order {
    position: absolute;
    left: 186px;
    top: 540px;
    width: 112px;
    height: 31px;
    border-radius: 5px;
    background: linear-gradient(180deg, #f0608f 0%, var(--pink-deep) 100%);
    box-shadow: 0 2px 3px rgba(0, 0, 0, 0.25);
    color: var(--white);
    font-family: "Jost", sans-serif;
    font-weight: 500;
    font-size: 12px;
    letter-spacing: 0.5px;
    display: flex;
    align-items: center;
  }
  .order__label { width: 80px; text-align: center; }
  .order__arrow {
    width: 32px;
    height: 100%;
    border-left: 1px solid rgba(255, 255, 255, 0.45);
    display: flex;
    align-items: center;
    justify-content: center;
  }
  .model {
    position: absolute;
    left: 496px;
    top: 58px;
    width: 180px;
    height: 522px;
    border-radius: 90px 90px 40px 40px;
    background: linear-gradient(180deg, #e0b59a 0%, #d3a0a8 30%, #e466a8 55%, #9a7cc8 70%, #eed2c4 100%);
  }
</style>
</head>
<body>
<main class="stage">
  <section class="banner">
    <svg class="backdrop" width="700" height="608" viewBox="0 0 700 608" aria-hidden="true">
      <path d="M0 130 C 150 100, 300 200, 700 170 L700 608 L0 608 Z" fill="#fbe3ee" opacity="0.6"/>
      <path d="M0 200 C 120 250, 260 330, 480 310 C 580 300, 650 270, 700 260 L700 608 L0 608 Z" fill="#f7c6dc" opacity="0.55"/>
      <path d="M40 608 C 80 540, 260 520, 420 560 C 520 585, 620 560, 700 520 L700 608 Z" fill="#ffffff" opacity="0.7"/>
      <path d="M0 330 C 160 300, 300 380, 520 340 C 600 325, 660 310, 700 300" fill="none" stroke="#ffffff" stroke-width="6" opacity="0.7"/>
    </svg>

    <div class="headline">Spring Has Sprung!</div>
    <h1 class="title title--one">New Season</h1>
    <h2 class="title title--two">New Sexy Dresses!</h2>
    <p class="tagline">A Style For Every Woman!</p>
    <svg class="underline" width="390" height="16" viewBox="0 0 390 16" aria-hidden="true">
      <path d="M2 10 C 80 4, 200 12, 300 6 C 340 4, 370 5, 388 3 L386 8 C 300 12, 200 14, 4 14 Z" fill="var(--pink)"/>
    </svg>

    <svg class="offers" width="520" height="150" viewBox="0 0 520 150" aria-hidden="true">
      <polygon points="0,0 442,0 508,148 0,148" fill="var(--pink-band)" opacity="0.92"/>
    </svg>
    <div class="step step--one">1</div>
    <div class="step step--two">2</div>
    <div class="offer offer--sale">
      <p class="offer__label">Shop Our Sales<br>Up To</p>
      <p class="offer__figure">60% off!</p>
    </div>
    <div class="offer offer--ship">
      <p class="offer__label">Free U.S. Shipping<br>On Orders Over</p>
      <p class="offer__figure">$75</p>
    </div>

    <div class="order">
      <span class="order__label">ORDER</span>
      <span class="order__arrow">
        <svg width="10" height="14" viewBox="0 0 10 14" aria-hidden="true"><path d="M2 2 L8 7 L2 12" fill="none" stroke="#ffffff" stroke-width="2.4" stroke-linecap="round"/></svg>
      </span>
    </div>

    <div class="model" role="img" aria-label="Photo of a smiling woman in a fitted pink and blue floral sleeveless dress, standing with hands on hips"></div>
  </section>
</main>
</body>
</html>
```